Kestrel Gardenworks Business Card

An eye catching, yet simple business card that includes;

1. our logo
2. office phone - 5083172946
3. email - kestrelgardenworks@mailbrook.com
4. website - www.kestrelgardenworks.com
5. instagram - @kestrelgardenworksnv

```html
<!DOCTYPE html>
<html lang="en">
<head>
<meta charset="utf-8">
<title>Kestrel Gardenworks Business Card</title>
<link rel="stylesheet" href="https://fonts.googleapis.com/css2?family=Open+Sans:wght@400;800&display=swap">
<style>
  :root {
    --backdrop: #222222;
    --earth: #9c5f2b;
    --ink: #211b18;
    --ink-soft: #3a2e27;
    --paper: #ffffff;
  }
  * { box-sizing: border-box; margin: 0; padding: 0; }
  html, body { width: 1200px; height: 780px; overflow: hidden; }
  body {
    background: var(--backdrop);
    font-family: "Open Sans", Arial, sans-serif;
    position: relative;
  }
  .card {
    position: absolute;
    top: 235px;
    width: 540px;
    height: 310px;
    overflow: hidden;
    box-shadow: 0 18px 40px rgba(0,0,0,.45);
  }
  .card-back { left: 40px; background: var(--paper); }
  .card-front { left: 620px; background: var(--earth); }

  /* front */
  .front-brand {
    position: absolute;
    inset: 0;
    display: flex;
    align-items: center;
    justify-content: center;
    gap: 14px;
  }
  .brand-dot {
    width: 26px; height: 26px;
    border-radius: 50%;
    background: var(--paper);
    flex: none;
  }
  .front-brand .brand-name {
    color: var(--paper);
    font-weight: 800;
    font-size: 38px;
    letter-spacing: .5px;
    line-height: 1;
  }

  /* back */
  .earth-band { position: absolute; inset: 0; }
  .back-brand {
    position: absolute;
    left: 24px; top: 62px;
    display: flex;
    align-items: center;
    gap: 8px;
    color: var(--ink);
    font-weight: 800;
    font-size: 15px;
    line-height: 1.15;
  }
  .back-brand .brand-dot {
    width: 14px; height: 14px;
    background: var(--earth);
  }
  .mascot-art {
    position: absolute;
    left: 200px; top: 36px;
    width: 300px; height: 118px;
    border-radius: 70px 110px 50px 80px;
    background: linear-gradient(150deg, var(--ink-soft), var(--ink) 70%);
  }
  .contact-list {
    position: absolute;
    right: 22px; bottom: 18px;
    list-style: none;
    color: var(--paper);
    font-size: 14px;
    text-align: right;
  }
  .contact-list li {
    display: flex;
    justify-content: flex-end;
    align-items: center;
    gap: 8px;
    line-height: 1.5;
  }
  .contact-icon { width: 13px; height: 13px; flex: none; }
</style>
</head>
<body>

<section class="card card-back" aria-label="Card back">
  <svg class="earth-band" viewBox="0 0 540 310" preserveAspectRatio="none" aria-hidden="true">
    <path d="M0 195 C110 188 190 168 290 172 C390 176 470 160 540 150 L540 310 L0 310 Z" fill="var(--earth)"/>
  </svg>
  <div class="back-brand">
    <span class="brand-dot" aria-hidden="true"></span>
    <span>Kestrel<br>Gardenworks</span>
  </div>
  <div class="mascot-art" role="img" aria-label="Dark silhouette of the brand's animal mascot stretching across the card"></div>
  <ul class="contact-list">
    <li>5083172946
      <svg class="contact-icon" viewBox="0 0 16 16" aria-hidden="true"><path d="M4 1 L6.5 4.5 L5 6.2 C6 8.3 7.7 10 9.8 11 L11.5 9.5 L15 12 L13.2 15 C7 14.5 1.5 9 1 2.8 Z" fill="var(--paper)"/></svg>
    </li>
    <li>@kestrelgardenworksnv
      <svg class="contact-icon" viewBox="0 0 16 16" aria-hidden="true"><circle cx="8" cy="8" r="7" fill="var(--paper)"/></svg>
    </li>
    <li>www.kestrelgardenworks.com
      <svg class="contact-icon" viewBox="0 0 16 16" aria-hidden="true"><circle cx="8" cy="8" r="6.5" fill="none" stroke="var(--paper)" stroke-width="1.6"/><path d="M1.5 8 H14.5 M8 1.5 C5 5 5 11 8 14.5 M8 1.5 C11 5 11 11 8 14.5" fill="none" stroke="var(--paper)" stroke-width="1.2"/></svg>
    </li>
    <li>kestrelgardenworks@mailbrook.com
      <svg class="contact-icon" viewBox="0 0 16 16" aria-hidden="true"><rect x="1" y="3" width="14" height="10" fill="none" stroke="var(--paper)" stroke-width="1.6"/><path d="M1 3 L8 9 L15 3" fill="none" stroke="var(--paper)" stroke-width="1.6"/></svg>
    </li>
  </ul>
</section>

<section class="card card-front" aria-label="Card front">
  <div class="front-brand">
    <span class="brand-dot" aria-hidden="true"></span>
    <span class="brand-name">Kestrel Gardenworks</span>
  </div>
</section>

</body>
</html>
```